Postcard Design/Coupon

My business is a Pizza Shop/Restaurant/Bar. I know confusing. I sell mainly pizza and beer but sandwich's and salads are a big seller also. So I want coupons/postcards that I can hand out to every table that comes in to entice them to come back. I also will be sending these coupons/postcards to delivery customers. The business name is Harlow Pizza Bella address is 318 Tamsin Lane Brindale PA17382 phone number is 412-741-1744On one side I wanted the coupon offer and logo and the other side the hours but also room for me to send some out.

Target Market(s)

Families

Industry/Entity Type

Restaurant

Requirements
Must have
• Pizza
Nice to have
• Salads/Hoagies/Nice Description

```html
<!DOCTYPE html>
<html lang="en">
<head>
<meta charset="utf-8">
<title>Harlow Pizza Bella – Postcard</title>
<link rel="stylesheet" href="https://fonts.googleapis.com/css2?family=Oswald:wght@500;600&family=Roboto+Condensed:wght@400;700&family=Chewy&display=swap">
<style>
  :root{
    --page:#2b2b2d;
    --orange-light:#f6a443;
    --orange:#e07a1c;
    --orange-deep:#b7510f;
    --brown:#6a2f0c;
    --green:#4a5530;
    --green-dark:#3c4526;
    --ink:#1d1a16;
    --cream:#fff6e6;
    --yellow:#ffe81a;
    --label-yellow:#f3e21f;
    --pink:#d94fa8;
    --white:#ffffff;
    --coupon-red:#e2501b;
  }
  *{box-sizing:border-box;margin:0;padding:0}
  html,body{width:1200px;height:1012px;overflow:hidden;background:var(--page)}
  body{position:relative;font-family:"Roboto Condensed",Arial,sans-serif}

  .card{position:absolute;left:230px;width:740px;overflow:hidden;box-shadow:0 8px 24px rgba(0,0,0,.45)}

  /* ---------- Front: coupon side ---------- */
  .card-front{top:22px;height:470px;
    background:radial-gradient(ellipse at 62% 35%,var(--orange-light) 0%,var(--orange) 45%,var(--orange-deep) 100%)}
  .beer-photo{position:absolute;left:40px;top:40px;width:250px;height:290px;border-radius:10px;
    background:linear-gradient(180deg,#fbf1e0 0%,#f3d9a8 18%,#c9651d 40%,#9c3d0e 100%)}
  .pizza-photo{position:absolute;left:270px;top:235px;width:450px;height:95px;border-radius:50% / 40%;
    background:radial-gradient(ellipse at 50% 45%,#7a3f1a 0%,#9d5a2a 55%,#e4c89b 80%,#f1dfbd 100%)}
  .front-brand{position:absolute;left:330px;top:36px;width:380px;text-align:center}
  .brand-name{font-family:"Oswald",Arial,sans-serif;font-weight:600;color:var(--green-dark);font-size:64px;line-height:1;letter-spacing:1px}
  .brand-sub{font-family:"Oswald",Arial,sans-serif;font-weight:600;color:var(--cream);font-size:20px;letter-spacing:3px;margin-top:4px}
  .front-hours{position:absolute;left:300px;top:158px;width:440px;text-align:center;color:var(--ink)}
  .front-hours .hours{font-family:"Oswald",Arial,sans-serif;font-weight:600;font-size:25px}
  .front-hours .address{font-size:15px;line-height:1.15;margin-top:2px}
  .order-band{position:absolute;left:0;right:0;bottom:0;height:140px;
    background:linear-gradient(180deg,var(--orange-deep) 0%,var(--orange) 100%)}
  .order-line{position:absolute;left:300px;top:350px;width:420px;color:var(--cream);font-size:24px;text-align:right}
  .coupon{position:absolute;left:40px;top:325px;width:230px;height:125px;background:var(--white);
    border:2px dashed #777;overflow:hidden}
  .coupon-amount{position:absolute;left:10px;top:6px;font-family:"Oswald",Arial,sans-serif;font-weight:600;font-size:40px;line-height:1;color:var(--ink)}
  .coupon-amount sup{font-size:24px}
  .coupon-amount small{font-size:22px}
  .coupon-brand{position:absolute;left:12px;top:56px;font-family:"Oswald",Arial,sans-serif;font-weight:600;font-size:17px;color:var(--green-dark);line-height:1}
  .coupon-pizza{position:absolute;right:8px;top:6px;width:118px;height:86px;border-radius:50%;
    background:radial-gradient(circle,#d9462a 0%,#c8362a 45%,#e3a95a 75%,#f2cf8a 100%)}
  .coupon-offer{position:absolute;left:0;right:0;bottom:0;height:30px;background:var(--coupon-red);
    color:var(--white);font-family:"Oswald",Arial,sans-serif;font-weight:600;font-size:19px;line-height:30px;padding-left:18px}

  /* ---------- Back: mailing side ---------- */
  .card-back{top:512px;height:470px;background:var(--white)}
  .return-bar{position:absolute;left:0;top:0;width:470px;height:70px;background:var(--green)}
  .return-address{position:absolute;right:16px;top:10px;text-align:right;color:var(--white);font-size:11px;line-height:1.3}
  .return-address strong{font-size:12px;letter-spacing:.5px}
  .promo-panel{position:absolute;left:0;top:70px;width:370px;height:260px;
    background:linear-gradient(90deg,var(--brown) 0%,var(--orange-deep) 55%,var(--orange) 100%)}
  .sandwich-photo{position:absolute;left:10px;top:-60px;width:260px;height:150px;border-radius:12px;
    background:linear-gradient(180deg,#d9a569 0%,#b97a3e 35%,#5f9a2e 60%,#e14a24 80%,#f0c23a 100%)}
  .label-fresh{position:absolute;left:40px;top:100px;width:230px;padding:4px 10px;background:var(--label-yellow);
    font-family:"Chewy",sans-serif;font-size:20px;line-height:1.05;color:var(--ink);text-align:center}
  .label-daily{position:absolute;left:190px;top:154px;padding:3px 14px;background:var(--pink);
    font-family:"Chewy",sans-serif;font-size:22px;line-height:1.2;color:var(--cream)}
  .back-brand{position:absolute;left:46px;top:198px;font-family:"Oswald",Arial,sans-serif;font-weight:600;color:var(--white);font-size:32px;line-height:1}
  .back-brand span{display:block;font-size:14px;letter-spacing:3px;margin-top:2px}
  .order-panel{position:absolute;left:0;top:330px;width:370px;height:140px;background:var(--green)}
  .order-panel .call{position:absolute;left:72px;top:16px;color:var(--white);font-size:22px}
  .order-panel .phone{position:absolute;left:72px;top:42px;color:var(--yellow);font-weight:700;font-size:30px;letter-spacing:1px}
  .order-panel .rule{position:absolute;left:0;right:0;top:90px;height:2px;background:var(--cream)}
  .order-panel .hours{position:absolute;left:60px;top:100px;color:var(--white);font-weight:700;font-size:18px}
</style>
</head>
<body>

<section class="card card-front" aria-label="Coupon side">
  <div class="beer-photo" role="img" aria-label="Photo of two glasses of beer with foam"></div>
  <div class="pizza-photo" role="img" aria-label="Photo of a loaded pizza on a wooden board"></div>

  <div class="front-brand">
    <div class="brand-name">Pizza Bella</div>
    <div class="brand-sub">PIZZERIA</div>
  </div>

  <div class="front-hours">
    <div class="hours">HOURS : 11:00 AM - 10:00 PM</div>
    <div class="address">HARLOW PIZZA BELLA<br>318 Tamsin Lane Brindale PA17382</div>
  </div>

  <div class="order-band"></div>
  <div class="order-line">To Place An Order Call: 555-208-3961</div>

  <div class="coupon">
    <div class="coupon-amount"><sup>$</sup>5<small>OFF</small></div>
    <div class="coupon-brand">Pizza Bella</div>
    <div class="coupon-pizza" role="img" aria-label="Photo of a whole pizza with peppers and mushrooms"></div>
    <div class="coupon-offer">ON ANY PIZZA</div>
  </div>
</section>

<section class="card card-back" aria-label="Mailing side">
  <div class="return-bar">
    <div class="return-address">
      <strong>HARLOW PIZZA BELLA</strong><br>
      318 Tamsin Lane<br>
      Brindale PA17382<br>
      555-208-3961
    </div>
  </div>

  <div class="promo-panel">
    <div class="sandwich-photo" role="img" aria-label="Photo of a toasted sandwich with lettuce, tomato and peppers"></div>
    <div class="label-fresh">Fresh Sandwiches<br>&amp; Salads</div>
    <div class="label-daily">Made Daily</div>
    <div class="back-brand">Pizza Bella<span>PIZZERIA</span></div>
  </div>

  <div class="order-panel">
    <div class="call">To Place Orders Call</div>
    <div class="phone">555-208-3961</div>
    <div class="rule"></div>
    <div class="hours">HOURS: 11:00 AM – 10:00 PM</div>
  </div>
</section>

</body>
</html>
```